Property Report

8 page document, similar theme to our website (www.harbourandvale.example) and previous brochure (provided). All content provided. We want a professional looking document. We need ASAP. Thanks!

Industry/Entity Type

Property

Font styles to use
Serif
Sans Serif

Colors
ffc214
ffcf3e
fee18a
fff3d1

Requirements
Must have
• Page 1: Cover
Page 2: Content
Page 3: About Us
Page 4: Site Description
Page 5: Scheme
Page 6: Analysis
Page 7: Conclusion
Page 8: Contact Details

```html
<!DOCTYPE html>
<html lang="en">
<head>
<meta charset="utf-8">
<title>Site Report – Harbour &amp; Vale Commercial</title>
<link rel="stylesheet" href="https://fonts.googleapis.com/css2?family=Lato:wght@400;700&family=Oswald:wght@500&display=swap">
<style>
  :root {
    --yellow: #ffc214;
    --yellow-mid: #ffcf3e;
    --yellow-soft: #fee18a;
    --cream: #fff3d1;
    --navy: #2e2c5e;
    --ink: #111111;
    --slate: #3c3f44;
    --slate-dark: #2a2c30;
    --rule: #6d6f73;
    --white: #ffffff;
  }
  * { margin: 0; padding: 0; box-sizing: border-box; }
  html, body { width: 1200px; height: 810px; overflow: hidden; background: var(--white); }
  body { position: relative; font-family: "Lato", sans-serif; }

  .spread { position: absolute; left: 66px; top: 59px; width: 1068px; height: 691px; }
  .page { position: absolute; top: 0; height: 691px; width: 534px; overflow: hidden; }
  .page--contents { left: 0; }
  .page--about { left: 534px; background: var(--yellow); }

  .cover-photo { position: absolute; inset: 0;
    background: linear-gradient(160deg, #55585d 0%, var(--slate) 45%, var(--slate-dark) 100%); }
  .divider-line { position: absolute; left: 267px; top: 132px; width: 2px; height: 523px; background: var(--rule); }

  .brand-name { position: absolute; left: 0; width: 534px; top: 42px; text-align: center;
    color: var(--white); font-weight: 700; font-size: 28px; line-height: 32px; }

  .contents-title { position: absolute; left: 156px; top: 300px; color: var(--yellow);
    font-weight: 700; font-size: 14px; line-height: 17px; }
  .contents-band { position: absolute; left: 0; top: 326px; width: 267px; height: 8px; background: var(--rule); }
  .contents-list { position: absolute; left: 156px; top: 374px; width: 220px; list-style: none; }
  .contents-list li { display: flex; justify-content: space-between; height: 28.8px;
    color: var(--yellow); font-size: 10px; line-height: 12px; }
  .contents-list .num { width: 10px; }

  .footer { position: absolute; top: 655px; height: 19px; display: flex; align-items: center;
    font-family: "Oswald", sans-serif; font-weight: 500; font-size: 9px; letter-spacing: 0.2px;
    color: var(--ink); text-transform: uppercase; white-space: nowrap; }
  .footer--left { left: 0; width: 534px; background: var(--yellow); }
  .footer--right { left: 0; width: 534px; background: var(--white); justify-content: flex-end; }
  .footer .folio { width: 37px; text-align: center; }
  .footer .sep { width: 1px; height: 19px; background: var(--ink); }
  .footer .label { padding: 0 9px; }

  .badge { position: absolute; left: 421px; top: 0; width: 77px; height: 65px; }
  .badge-name { position: absolute; left: 421px; top: 12px; width: 77px; text-align: center;
    color: var(--white); font-weight: 700; font-size: 10px; line-height: 12px; }

  .about-title { position: absolute; left: 219px; top: 174px; font-weight: 700; font-size: 22px; line-height: 26px; color: var(--ink); }
  .about-copy { position: absolute; left: 219px; top: 218px; width: 174px;
    font-size: 9px; line-height: 11.6px; color: var(--ink); }
  .about-copy p + p { margin-top: 17px; }

  .skyline { position: absolute; left: 146px; top: 273px; width: 388px; height: 418px;
    background: linear-gradient(180deg, rgba(255,207,62,0) 0%, var(--yellow-mid) 45%, var(--yellow-soft) 100%);
    clip-path: polygon(0 80%, 25% 80%, 25% 45%, 50% 40%, 60% 12%, 70% 12%, 78% 0, 100% 18%, 100% 100%, 0 100%); }
</style>
</head>
<body>
  <div class="spread">
    <section class="page page--contents">
      <div class="cover-photo" role="img" aria-label="Black and white photograph of a modernist apartment block facade with balconies"></div>
      <div class="divider-line"></div>
      <div class="brand-name">Harbour &amp; Vale<br>Commercial</div>

      <h2 class="contents-title">Content</h2>
      <div class="contents-band"></div>
      <ul class="contents-list">
        <li><span>About Us</span><span class="num">3</span></li>
        <li><span>Site Description</span><span class="num">4</span></li>
        <li><span>Scheme</span><span class="num">5</span></li>
        <li><span>Analysis</span><span class="num">6</span></li>
        <li><span>Conclusion</span><span class="num">7</span></li>
        <li><span>Contact Details</span><span class="num">8</span></li>
      </ul>

      <div class="footer footer--left">
        <span class="folio">02</span><span class="sep"></span>
        <span class="label">Site Report &nbsp;|&nbsp; 17 Example Lane, Northfield KT9 2ZZ</span>
      </div>
    </section>

    <section class="page page--about">
      <div class="skyline" role="img" aria-label="Line illustration of city tower blocks"></div>

      <svg class="badge" viewBox="0 0 77 65" aria-hidden="true">
        <polygon points="0,0 77,0 77,57 38.5,65 0,57" fill="var(--navy)"/>
      </svg>
      <div class="badge-name">Harbour &amp; Vale<br>Commercial</div>

      <h1 class="about-title">About Us</h1>
      <div class="about-copy">
        <p>Text: Harbour &amp; Vale Commercial specialise in the acquisition and disposal of development, investment and commercial property in London and the Home Counties. Our consultants advise on a wide range of property types and use classes and are experts in identifying ways in which property owners can maximise value.</p>
        <p>Our considerable knowledge of the property market and creative approach to delivering maximum value, has enabled us to become one of the most active development and investment consultancies in London and the South East.</p>
      </div>

      <div class="footer footer--right">
        <span class="label">www.harbourandvale.example</span><span class="sep"></span>
        <span class="folio">03</span>
      </div>
    </section>
  </div>
</body>
</html>
```